1. Overview of company:
Copper Fern Mobile solutions private Ltd is one of the leading innovators & providers of Value added services (VAS) and telecom solutions to the top telecom operators across the world. We are the pioneer of several telecom technologies and products with our solutions empowering over 40 telecom giant in 51 countries.

2. Product Overview:
Vocal Twist is the most innovative voice morphing mobile app that has revolutionized the concept of IVR based offerings for telecom operators across the world. It lets you talk to your friend in a voice of your choice at just the press of a button. In addition to every call, users can now speak to their friends with background sounds of their choice.

In simple words: If person A calls person B, person A can choose the voice he wants B to listen, Words and sentences remain same just the voice changes. Person A can even activate a background sound for both of them while talking.

3. Objective of the design:
The purpose of this campaign is to establish Vocal Twist as Innovative, Lively, Youthful, Fun mobile app generally used for spreading smiles via pranks. The primary objective is to persuade the audience to download and use Vocal Twist mobile app, as well as to spread and characterize this new app.

4. Product layout:
Page 1: Landing Page
- pictorial explanation, what Vocal Twist stands for

Page 2: Home Screen options
-Navigation to vocal twist
-Navigation to sound scenery

Page 3: Vocal Twist options
-Female
-Cartoon
-King
-Bunny

Page 4: Sound scenery options
-Romantic
-Airport
-Traffic
-Football
-Church
-Beach

5. Target Audience
The users of the mobile app will be teenager whose age ranges from 16-27. The demographics are not restricted to a particular country and will be present on global level.

6. Deliverable
- 4 Uncoded screen and icon for mobile app "Vocal Twist"
- Our company name is "Copper Fern" , we would like to see designs that use Black and Green, at the same time its not mandatory.
-Design should communicate what the app stands for "Changing voice of caller"

Target Market(s)

User of the mobile app will be teenagers whose age ranges from 16-27. The demographics are not restricted to a particular country and will be present on global level. It's for masses.

Industry/Entity Type

Telecommunications

Requirements
Must have
• The design should be self explanatory, what the app stands for.
• Editable format for integration purpose.
Nice to have
• Would prefer Icons and very few words.
• Professional, elegant at the same time trendy designs.

```html
<!DOCTYPE html>
<html lang="en">
<head>
<meta charset="utf-8">
<title>Vocal Twist App – Screens</title>
<link rel="stylesheet" href="https://fonts.googleapis.com/css2?family=Oswald:wght@400;500;600;700&display=swap">
<style>
:root{
  --green:#8cc63f;
  --ink:#1c1c1c;
  --screen-bg:#d9dad1;
  --tile:#f7f7f4;
  --track:#c9cac3;
  --muted:#a8a9a2;
  --white:#ffffff;
}
*{box-sizing:border-box;margin:0;padding:0}
html,body{width:1200px;height:900px;overflow:hidden;background:var(--white)}
body{position:relative;font-family:"Oswald",sans-serif;color:var(--ink)}
.page-title{position:absolute;top:105px;left:0;width:1200px;text-align:center;font-size:74px;font-weight:700;letter-spacing:-1px;line-height:1}
.page-title .accent{color:var(--green)}
.icon-defs{position:absolute;width:0;height:0}

.screen{position:absolute;top:325px;width:233px;height:405px;background:var(--screen-bg);overflow:hidden}
.screen-header{position:absolute;top:0;left:0;width:233px;height:40px;background:var(--white);display:flex;align-items:center;justify-content:center;gap:5px}
.brand-mark{width:10px;height:10px;background:var(--green)}
.brand-name{font-size:9px;font-weight:500;letter-spacing:.6px}

.section-bar{position:absolute;left:19px;width:195px;height:22px;background:var(--ink);color:var(--white);font-size:12.5px;font-weight:600;display:flex;align-items:center;justify-content:center;gap:4px;box-shadow:0 1px 2px rgba(0,0,0,.25)}
.section-bar .accent{color:var(--green)}
.section-bar.is-active{background:var(--green)}
.section-bar.is-active .accent{color:var(--white)}

.icon-row{position:absolute;left:19px;width:195px;height:33px;display:flex;gap:7.5px}
.icon-tile{width:33px;height:33px;background:var(--tile);display:flex;align-items:center;justify-content:center;box-shadow:0 1px 2px rgba(0,0,0,.2);font-size:6.5px;font-weight:600}
.icon-tile svg{width:22px;height:22px;fill:none;stroke:var(--ink);stroke-width:1.3;stroke-linejoin:round;stroke-linecap:round}
.icon-tile.is-selected{background:var(--green)}
.icon-tile.is-selected svg{stroke:var(--white)}
.icon-placeholder{width:21px;height:21px;border-radius:50%;background:linear-gradient(#cfd0c9,#b9bab3)}
.is-selected .icon-placeholder{background:rgba(255,255,255,.7)}

.level-box{position:absolute;left:19px;width:195px;height:32px;background:var(--tile);box-shadow:0 1px 2px rgba(0,0,0,.2)}
.level-label{position:absolute;top:4px;left:0;width:100%;text-align:center;font-size:7px;font-weight:600}
.level-label .prefix{color:var(--muted)}
.level-control{position:absolute;top:14px;left:8px;right:8px;height:14px;display:flex;align-items:center;gap:8px;font-size:13px;font-weight:400}
.level-control .sign{width:10px;text-align:center;color:var(--ink)}
.level-control.is-disabled .sign{color:var(--track)}
.level-track{flex:1;height:3px;background:var(--track);position:relative}
.level-fill{position:absolute;left:0;top:0;height:3px;background:var(--green)}

.preview-row{position:absolute;left:19px;top:313px;width:195px;height:32px}
.preview-label{position:absolute;top:0;left:8px;font-size:6.5px;font-weight:600}
.preview-label.is-muted{color:var(--muted)}
.record-dot{position:absolute;top:13px;left:12px;width:18px;height:18px;border-radius:50%;background:var(--ink)}
.record-dot.is-live{background:var(--green)}
.player{position:absolute;top:10px;left:61px;width:134px;height:20px;background:var(--tile);display:flex;align-items:center;gap:5px;padding:0 7px}
.player-time{position:absolute;top:-9px;left:62px;font-size:6.5px;font-weight:600}
.play-icon{width:0;height:0;border-top:4px solid transparent;border-bottom:4px solid transparent;border-left:7px solid var(--track)}
.play-icon.is-on{border-left-color:var(--ink)}
.player-track{flex:1;height:3px;background:var(--track);position:relative}

.tab-bar{position:absolute;left:19px;top:362px;width:195px;height:42px;background:var(--green);display:flex}
.tab{flex:1;display:flex;flex-direction:column;align-items:center;justify-content:center;gap:2px;color:var(--white);font-size:6px;font-weight:600}
.tab svg{width:20px;height:20px;fill:none;stroke:var(--white);stroke-width:1.3;stroke-linejoin:round;stroke-linecap:round}
.tab.is-current{background:var(--white);color:var(--ink)}
.tab.is-current svg{stroke:var(--ink)}
</style>
</head>
<body>

<h1 class="page-title">VOCAL <span class="accent">TWIST</span> App</h1>

<svg class="icon-defs" aria-hidden="true">
  <symbol id="i-crown" viewBox="0 0 24 24"><path d="M3 18V7l5 5 4-7 4 7 5-5v11z"/><path d="M5 15h14"/></symbol>
  <symbol id="i-heart" viewBox="0 0 24 24"><path d="M12 20 4 12a4.5 4.5 0 0 1 8-5 4.5 4.5 0 0 1 8 5z"/></symbol>
  <symbol id="i-plane" viewBox="0 0 24 24"><path d="M12 3c1 0 1.3 1.5 1.3 3v4l8 4.5v1.5l-8-2.5v4l2.5 2v1.3L12 20l-3.8 1v-1.3l2.5-2v-4l-8 2.5v-1.5l8-4.5V6c0-1.5.3-3 1.3-3z"/></symbol>
  <symbol id="i-traffic" viewBox="0 0 24 24"><rect x="8" y="3" width="8" height="17" rx="1.5"/><circle cx="12" cy="7" r="1.6"/><circle cx="12" cy="11.5" r="1.6"/><circle cx="12" cy="16" r="1.6"/><path d="M8 7H5M8 11.5H5M8 16H5M16 7h3M16 11.5h3M16 16h3M12 20v2"/></symbol>
  <symbol id="i-ball" viewBox="0 0 24 24"><circle cx="12" cy="12" r="8.5"/><path d="m12 8.5 3.2 2.3-1.2 3.7h-4l-1.2-3.7z"/><path d="M12 3.5v5M15.2 10.8l4.5-1.5M14 14.5l2.8 3.8M10 14.5l-2.8 3.8M8.8 10.8 4.3 9.3"/></symbol>
  <symbol id="i-church" viewBox="0 0 24 24"><path d="M12 2v5M10 4h4M3 13l9-6 9 6M5 12v9h14v-9"/><path d="M10 21v-4a2 2 0 0 1 4 0v4"/></symbol>
  <symbol id="i-beach" viewBox="0 0 24 24"><path d="M3 13a8 8 0 0 1 14-4z"/><path d="M10 11l5 10M3 21h16"/><circle cx="19" cy="5" r="1.5"/><path d="M19 1.5v1M19 7.5v1M22.5 5h-1M16.5 5h-1"/></symbol>
  <symbol id="i-home" viewBox="0 0 24 24"><path d="M3 11 12 3l9 8M5 9.5V21h5v-6h4v6h5V9.5"/></symbol>
  <symbol id="i-morph" viewBox="0 0 24 24"><path d="M3 7h4c4 0 6 10 10 10h4M3 17h4c4 0 6-10 10-10h4M18 4l3 3-3 3M18 14l3 3-3 3"/></symbol>
  <symbol id="i-mic" viewBox="0 0 24 24"><rect x="9" y="3" width="6" height="11" rx="3"/><path d="M6 11a6 6 0 0 0 12 0M12 17v4M9 21h6"/></symbol>
  <symbol id="i-call" viewBox="0 0 24 24"><path d="M6 3h3l1.5 4.5-2 1.5a11 11 0 0 0 6.5 6.5l1.5-2L21 15v3a2 2 0 0 1-2 2A16 16 0 0 1 4 5a2 2 0 0 1 2-2z"/></symbol>
  <symbol id="i-gear" viewBox="0 0 24 24"><circle cx="12" cy="12" r="3"/><path d="M12 2.5l1.6 2.6 3-.8.8 3 2.6 1.6-1.4 2.6 1.4 2.6-2.6 1.6-.8 3-3-.8L12 21.5l-1.6-2.6-3 .8-.8-3-2.6-1.6L5.4 12 4 9.4l2.6-1.6.8-3 3 .8z"/></symbol>
</svg>

<!-- Screen 1: idle -->
<section class="screen" style="left:75px">
  <header class="screen-header"><span class="brand-mark"></span><span class="brand-name">Copper Fern</span></header>
  <div class="section-bar" style="top:50px">CHOOSE YOUR <span class="accent">VOICE</span></div>
  <div class="icon-row" style="top:79px">
    <div class="icon-tile"><div class="icon-placeholder" role="img" aria-label="Female voice icon"></div></div>
    <div class="icon-tile"><div class="icon-placeholder" role="img" aria-label="Cartoon voice icon"></div></div>
    <div class="icon-tile"><svg><use href="#i-crown"/></svg></div>
    <div class="icon-tile"><div class="icon-placeholder" role="img" aria-label="Bunny voice icon"></div></div>
    <div class="icon-tile">MORE</div>
  </div>
  <div class="level-box" style="top:121px">
    <div class="level-label">VOICE DISTORTION LEVEL</div>
    <div class="level-control is-disabled"><span class="sign">−</span><div class="level-track"></div><span class="sign">+</span></div>
  </div>
  <div class="section-bar" style="top:161px">SELECT AN <span class="accent">AMBIANCE</span></div>
  <div class="icon-row" style="top:190px">
    <div class="icon-tile"><svg><use href="#i-heart"/></svg></div>
    <div class="icon-tile"><svg><use href="#i-plane"/></svg></div>
    <div class="icon-tile"><svg><use href="#i-traffic"/></svg></div>
    <div class="icon-tile"><svg><use href="#i-ball"/></svg></div>
    <div class="icon-tile"><svg><use href="#i-church"/></svg></div>
  </div>
  <div class="icon-row" style="top:231px">
    <div class="icon-tile"><svg><use href="#i-beach"/></svg></div>
    <div class="icon-tile">MORE</div>
  </div>
  <div class="level-box" style="top:272px">
    <div class="level-label">AMBIANCE VOLUME</div>
    <div class="level-control is-disabled"><span class="sign">−</span><div class="level-track"></div><span class="sign">+</span></div>
  </div>
  <div class="preview-row">
    <span class="preview-label">PREVIEW</span><span class="record-dot"></span>
    <div class="player"><span class="play-icon"></span><div class="player-track"><div class="level-fill" style="width:50%;background:#b5b6ae"></div></div></div>
  </div>
  <nav class="tab-bar">
    <div class="tab"><svg><use href="#i-home"/></svg>HOME</div>
    <div class="tab is-current"><svg><use href="#i-morph"/></svg>MORPH</div>
    <div class="tab"><svg><use href="#i-mic"/></svg>RECORD</div>
    <div class="tab"><svg><use href="#i-call"/></svg>CALL</div>
    <div class="tab"><svg><use href="#i-gear"/></svg>SETTINGS</div>
  </nav>
</section>

<!-- Screen 2: voice chosen -->
<section class="screen" style="left:348px">
  <header class="screen-header"><span class="brand-mark"></span><span class="brand-name">Copper Fern</span></header>
  <div class="section-bar is-active" style="top:50px">CHOOSE YOUR <span class="accent">VOICE</span></div>
  <div class="icon-row" style="top:79px">
    <div class="icon-tile"><div class="icon-placeholder" role="img" aria-label="Female voice icon"></div></div>
    <div class="icon-tile"><div class="icon-placeholder" role="img" aria-label="Cartoon voice icon"></div></div>
    <div class="icon-tile is-selected"><svg><use href="#i-crown"/></svg></div>
    <div class="icon-tile"><div class="icon-placeholder" role="img" aria-label="Bunny voice icon"></div></div>
    <div class="icon-tile">MORE</div>
  </div>
  <div class="level-box" style="top:121px">
    <div class="level-label"><span class="prefix">KING:</span> VOICE DISTORTION LEVEL</div>
    <div class="level-control"><span class="sign">−</span><div class="level-track"><div class="level-fill" style="width:55%"></div></div><span class="sign">+</span></div>
  </div>
  <div class="section-bar" style="top:161px">SELECT <span class="accent">AN AMBIANCE</span></div>
  <div class="icon-row" style="top:190px">
    <div class="icon-tile"><svg><use href="#i-heart"/></svg></div>
    <div class="icon-tile"><svg><use href="#i-plane"/></svg></div>
    <div class="icon-tile"><svg><use href="#i-traffic"/></svg></div>
    <div class="icon-tile"><svg><use href="#i-ball"/></svg></div>
    <div class="icon-tile"><svg><use href="#i-church"/></svg></div>
  </div>
  <div class="icon-row" style="top:231px">
    <div class="icon-tile"><svg><use href="#i-beach"/></svg></div>
    <div class="icon-tile">MORE</div>
  </div>
  <div class="level-box" style="top:272px">
    <div class="level-label">AMBIANCE VOLUME</div>
    <div class="level-control is-disabled"><span class="sign">−</span><div class="level-track"></div><span class="sign">+</span></div>
  </div>
  <div class="preview-row">
    <span class="preview-label">PREVIEW</span><span class="record-dot"></span>
    <div class="player"><span class="play-icon"></span><div class="player-track"></div></div>
  </div>
  <nav class="tab-bar">
    <div class="tab"><svg><use href="#i-home"/></svg>HOME</div>
    <div class="tab is-current"><svg><use href="#i-morph"/></svg>MORPH</div>
    <div class="tab"><svg><use href="#i-mic"/></svg>RECORD</div>
    <div class="tab"><svg><use href="#i-call"/></svg>CALL</div>
    <div class="tab"><svg><use href="#i-gear"/></svg>SETTINGS</div>
  </nav>
</section>

<!-- Screen 3: recording -->
<section class="screen" style="left:621px">
  <header class="screen-header"><span class="brand-mark"></span><span class="brand-name">Copper Fern</span></header>
  <div class="section-bar is-active" style="top:50px">CHOOSE YOUR <span class="accent">VOICE</span></div>
  <div class="icon-row" style="top:79px">
    <div class="icon-tile"><div class="icon-placeholder" role="img" aria-label="Female voice icon"></div></div>
    <div class="icon-tile"><div class="icon-placeholder" role="img" aria-label="Cartoon voice icon"></div></div>
    <div class="icon-tile is-selected"><svg><use href="#i-crown"/></svg></div>
    <div class="icon-tile"><div class="icon-placeholder" role="img" aria-label="Bunny voice icon"></div></div>
    <div class="icon-tile">MORE</div>
  </div>
  <div class="level-box" style="top:121px">
    <div class="level-label"><span class="prefix">KING:</span> VOICE DISTORTION LEVEL</div>
    <div class="level-control"><span class="sign">−</span><div class="level-track"><div class="level-fill" style="width:55%"></div></div><span class="sign">+</span></div>
  </div>
  <div class="section-bar is-active" style="top:161px">SELECT AN <span class="accent">AMBIANCE</span></div>
  <div class="icon-row" style="top:190px">
    <div class="icon-tile"><svg><use href="#i-heart"/></svg></div>
    <div class="icon-tile is-selected"><svg><use href="#i-plane"/></svg></div>
    <div class="icon-tile"><svg><use href="#i-traffic"/></svg></div>
    <div class="icon-tile"><svg><use href="#i-ball"/></svg></div>
    <div class="icon-tile"><svg><use href="#i-church"/></svg></div>
  </div>
  <div class="icon-row" style="top:231px">
    <div class="icon-tile"><svg><use href="#i-beach"/></svg></div>
    <div class="icon-tile">MORE</div>
  </div>
  <div class="level-box" style="top:272px">
    <div class="level-label"><span class="prefix">AIRPORT:</span> AMBIANCE VOL.</div>
    <div class="level-control"><span class="sign">−</span><div class="level-track"><div class="level-fill" style="width:55%"></div></div><span class="sign">+</span></div>
  </div>
  <div class="preview-row">
    <span class="preview-label is-muted">RECORDING...</span><span class="record-dot is-live"></span>
    <span class="player-time" style="left:122px">0:12</span>
    <div class="player"><span class="play-icon"></span><div class="player-track"></div></div>
  </div>
  <nav class="tab-bar">
    <div class="tab"><svg><use href="#i-home"/></svg>HOME</div>
    <div class="tab is-current"><svg><use href="#i-morph"/></svg>MORPH</div>
    <div class="tab"><svg><use href="#i-mic"/></svg>RECORD</div>
    <div class="tab"><svg><use href="#i-call"/></svg>CALL</div>
    <div class="tab"><svg><use href="#i-gear"/></svg>SETTINGS</div>
  </nav>
</section>

<!-- Screen 4: playing -->
<section class="screen" style="left:894px">
  <header class="screen-header"><span class="brand-mark"></span><span class="brand-name">Copper Fern</span></header>
  <div class="section-bar is-active" style="top:50px">CHOOSE YOUR <span class="accent">VOICE</span></div>
  <div class="icon-row" style="top:79px">
    <div class="icon-tile"><div class="icon-placeholder" role="img" aria-label="Female voice icon"></div></div>
    <div class="icon-tile"><div class="icon-placeholder" role="img" aria-label="Cartoon voice icon"></div></div>
    <div class="icon-tile is-selected"><svg><use href="#i-crown"/></svg></div>
    <div class="icon-tile"><div class="icon-placeholder" role="img" aria-label="Bunny voice icon"></div></div>
    <div class="icon-tile">MORE</div>
  </div>
  <div class="level-box" style="top:121px">
    <div class="level-label"><span class="prefix">KING:</span> VOICE DISTORTION LEVEL</div>
    <div class="level-control"><span class="sign">−</span><div class="level-track"><div class="level-fill" style="width:55%"></div></div><span class="sign">+</span></div>
  </div>
  <div class="section-bar is-active" style="top:161px">SELECT AN <span class="accent">AMBIANCE</span></div>
  <div class="icon-row" style="top:190px">
    <div class="icon-tile"><svg><use href="#i-heart"/></svg></div>
    <div class="icon-tile is-selected"><svg><use href="#i-plane"/></svg></div>
    <div class="icon-tile"><svg><use href="#i-traffic"/></svg></div>
    <div class="icon-tile"><svg><use href="#i-ball"/></svg></div>
    <div class="icon-tile"><svg><use href="#i-church"/></svg></div>
  </div>
  <div class="icon-row" style="top:231px">
    <div class="icon-tile"><svg><use href="#i-beach"/></svg></div>
    <div class="icon-tile">MORE</div>
  </div>
  <div class="level-box" style="top:272px">
    <div class="level-label"><span class="prefix">AIRPORT:</span> AMBIANCE VOL.</div>
    <div class="level-control"><span class="sign">−</span><div class="level-track"><div class="level-fill" style="width:55%"></div></div><span class="sign">+</span></div>
  </div>
  <div class="preview-row">
    <span class="preview-label is-muted">PLAYING...</span><span class="record-dot"></span>
    <span class="player-time" style="left:122px">0:06</span>
    <div class="player"><span class="play-icon is-on"></span><div class="player-track"><div class="level-fill" style="width:50%"></div></div></div>
  </div>
  <nav class="tab-bar">
    <div class="tab"><svg><use href="#i-home"/></svg>HOME</div>
    <div class="tab is-current"><svg><use href="#i-morph"/></svg>MORPH</div>
    <div class="tab"><svg><use href="#i-mic"/></svg>RECORD</div>
    <div class="tab"><svg><use href="#i-call"/></svg>CALL</div>
    <div class="tab"><svg><use href="#i-gear"/></svg>SETTINGS</div>
  </nav>
</section>

</body>
</html>
```